Bright-loop designs Business Card

embroidery printing

Target Market(s)

Businesses and public

Industry/Entity Type

Business

Contact Information for Business Card

Front of card..... Bright-loop designs .... Corin Maltby..... 868 512-7361.... Email... bright_loopdesigns@mailbrook.net

Back of card..... Bright-loop designs embroidery & artwork

Colors
000000

```html
<!DOCTYPE html>
<html lang="en">
<head>
<meta charset="utf-8">
<title>Bright-loop designs Business Card</title>
<link rel="stylesheet" href="https://fonts.googleapis.com/css2?family=Open+Sans:wght@400;600;700&display=swap">
<style>
  :root {
    --canvas: #d9d6d2;
    --card-black: #0b0b0b;
    --card-brown: #87421f;
    --accent-brown: #a5532a;
    --white: #ffffff;
    --soft-white: #ececec;
  }
  * { margin: 0; padding: 0; box-sizing: border-box; }
  html, body {
    width: 1200px; height: 900px; overflow: hidden;
    background: var(--canvas);
    font-family: "Open Sans", Arial, sans-serif;
  }
  .stage {
    position: relative; width: 1200px; height: 900px;
    display: flex; align-items: center; justify-content: center; gap: 40px;
  }
  .card {
    position: relative; width: 540px; height: 310px;
    border-radius: 4px;
    box-shadow: 0 10px 24px rgba(0,0,0,0.25);
  }
  .card--front { background: var(--card-black); }
  .card--back {
    background: var(--card-brown);
    display: flex; flex-direction: column; align-items: center; justify-content: center;
  }
  .brand-name {
    font-weight: 700; color: var(--white);
    letter-spacing: 0.5px; white-space: nowrap;
  }
  .card--front .brand-name {
    position: absolute; left: 150px; top: 96px; font-size: 34px;
  }
  .card--back .brand-name { font-size: 38px; }
  .tagline {
    margin-top: 22px; font-size: 15px; font-weight: 700; color: var(--white);
  }
  .holder-name {
    position: absolute; left: 44px; top: 218px;
    font-size: 17px; font-weight: 600; color: var(--accent-brown);
  }
  .divider {
    position: absolute; left: 190px; top: 186px;
    width: 1px; height: 62px; background: var(--accent-brown);
  }
  .contact-list {
    position: absolute; left: 204px; top: 190px;
    list-style: none; font-size: 13px; color: var(--soft-white);
  }
  .contact-list li { display: flex; align-items: center; gap: 8px; height: 22px; }
  .contact-icon { width: 11px; height: 11px; flex: none; }
</style>
</head>
<body>
  <main class="stage">
    <section class="card card--front" aria-label="Front of card">
      <div class="brand-name">Bright-loop designs</div>
      <p class="holder-name">Corin Maltby</p>
      <span class="divider"></span>
      <ul class="contact-list">
        <li>
          <svg class="contact-icon" viewBox="0 0 24 24" aria-hidden="true">
            <path fill="#a5532a" d="M6.6 10.8a15.1 15.1 0 0 0 6.6 6.6l2.2-2.2a1 1 0 0 1 1-.25 11.4 11.4 0 0 0 3.6.6 1 1 0 0 1 1 1V20a1 1 0 0 1-1 1A17 17 0 0 1 3 4a1 1 0 0 1 1-1h3.5a1 1 0 0 1 1 1c0 1.25.2 2.45.6 3.6a1 1 0 0 1-.25 1z"/>
          </svg>
          <span>868 512-7361</span>
        </li>
        <li>
          <svg class="contact-icon" viewBox="0 0 24 24" aria-hidden="true">
            <rect x="2" y="5" width="20" height="14" rx="1.5" fill="#a5532a"/>
            <path d="M3 6.5l9 6.5 9-6.5" fill="none" stroke="#0b0b0b" stroke-width="1.8"/>
          </svg>
          <span>bright_loopdesigns@mailbrook.net</span>
        </li>
      </ul>
    </section>

    <section class="card card--back" aria-label="Back of card">
      <div class="brand-name">Bright-loop designs</div>
      <p class="tagline">Embroidery &amp; Artwork</p>
    </section>
  </main>
</body>
</html>
```